Web design for facial expression recognition service

We offer a service which allows customers to film large panels of participants looking at some video/screen (e.g. an advertisement) and to analyze the facial expressions shown by the participants. We are looking for the design of a new website which will make it easy for our customers to setup and view the results of these experiments online.
Competitor's websites that may serve as a reference are:
http://www.moodlarkin.com/vexpo/#pane_overview
http://www.glimtorvo.com/homepage.aspx
https://www.panbrisk.com/
The website will (for as far as the design is concerned) consist of three parts:
- A public home page (and perhaps some contact/news/about page), designed to catch the attention/interest potential customers.
- A (protected) project result page, showing the results in an interactive page with charts and numerical data.
- Pages (also protected) with fields and tables (setting up the project details).
The winner of this design project should provide us with at least one design for each of the above in order to get a complete 'theme' going which our developers can use. However, you are welcome to initially only provide the design for the project result page and/or home page.
We are looking for a modern, fresh, yet professional look (my client is a more established party in the field).
The final delivery should consist of layered Photoshop or Illustrator files.
Thank you in advance for participating!
Reason: Extending the deadline by a few days to give designers a chance to submit designs for the other pages and process further feedback.
Target Market(s)
marketing research agencies (B2B service)
Industry/Entity Type
Delivery
Requirements
Must have
- Home page:
- Basic advertisement of the service; some quick explanation of how it works
- A way to login for existing users
- A link/button/banner inviting people to sign up
- Navigation controls to 2-3 other pages
- Social media links (Chatterloom, Workvine group)
- Company logo (sorry, can't provide it as my client wishes to remain anonymous for now, but it's rounded and has blue as it's main color).
- Copyright / creator details
Project result page:
(see attachment 1 for a functional mockup - the design may follow this layout closely, or be completely different)
- Title
- A video player and basic numerical data
- Different views of the analysis results can dynamically be added/removed/collapsed/expanded; each one of these views will show some kind of chart, filters (combos), numerical data and a download button/link.
- A way to sign out, go to the main project page and go to the main page
- Logo
- Copyright
The form pages:
(see attachment 2 for a functional mockup of one of the pages; feel free to change some elements to better show the overall style)
- Title
- Text fields, combos, calendar pickers, tables, navigation links
- Logo
- Copyright
Nice to have
- Any creative text elements or product logo/symbol are a bonus. However, the basic "Lorem Ipsum" would do too.

```html
<!DOCTYPE html>
<html lang="en">
<head>
<meta charset="utf-8">
<title>Lumivo – Project Result</title>
<link href="https://fonts.googleapis.com/css2?family=Arvo&family=Arimo:wght@400;700&family=Open+Sans:wght@400;600;700&display=swap" rel="stylesheet">
<style>
:root{
  --brand:#0a7cff;
  --brand-dark:#0864cc;
  --nav-edge:#1a1a1a;
  --side:#222;
  --page:#e9e9e9;
  --ink:#333;
  --panel:#fff;
  --plot:#f4f4f4;
  --grid:#c4c4c4;
  --legend:#d9d9d9;
  --green:#a9d38f;
  --blue:#9fbfe0;
  --red:#f45a5a;
  --pink:#f055c8;
  --marker:#d99a14;
}
*{box-sizing:border-box;margin:0;padding:0}
html,body{width:1200px;height:904px;overflow:hidden}
body{position:relative;background:var(--page);font-family:"Arimo",Arial,sans-serif;color:var(--ink)}
.abs{position:absolute}
.side-rail{left:0;top:0;width:89px;height:904px;background:var(--side)}
.side-rail .rail-top{position:absolute;left:0;top:0;width:89px;height:79px;background:var(--brand-dark)}
.side-rail .rail-nav{position:absolute;left:0;top:79px;width:89px;height:64px;background:var(--nav-edge)}
.collapse-arrow{left:70px;top:395px;width:0;height:0;border-top:19px solid transparent;border-bottom:19px solid transparent;border-right:18px solid #c9c9c9}
.top-bar{left:89px;top:0;width:1111px;height:79px;background:var(--brand)}
.brand-name{left:141px;top:26px;font-family:"Arimo",sans-serif;font-weight:400;font-size:26px;color:#fff}
.main-nav{left:89px;top:79px;width:1111px;height:64px;background:linear-gradient(#2e2e2e,#1f1f1f);box-shadow:0 2px 3px rgba(0,0,0,.3)}
.nav-link{top:101px;font-family:"Open Sans",sans-serif;font-size:14px;font-weight:700;color:#fff}
.caret{left:366px;top:109px;border-left:4px solid transparent;border-right:4px solid transparent;border-top:4px solid #ccc}
.avatar{left:1114px;top:95px;width:32px;height:32px;background:#9a9a9a;border:1px solid #bbb}
.user-name{left:1161px;top:102px;font-family:"Open Sans",sans-serif;font-size:13px;font-weight:700;color:#fff;white-space:nowrap}
.page-title{left:196px;top:184px;font-family:"Arvo",serif;font-weight:400;font-size:34px;line-height:48px;color:#4a4a4a}
.meta{left:198px;top:292px;font-size:13px;color:#222}
.meta span{margin-right:22px}
.divider{left:137px;top:343px;width:1063px;height:5px;border-top:1px solid #c8c8c8;border-bottom:1px solid #c8c8c8}
.view-title{left:168px;top:384px;font-size:19px;font-weight:700;color:#333}
.view-desc{left:168px;top:418px;font-size:12px;color:#333}
.delete-btn{left:1137px;top:388px;width:80px;height:45px;background:#dcdcdc;border-radius:4px}
.select{height:29px;background:linear-gradient(#fff,#f0f0f0);border:1px solid #c6c6c6;border-radius:3px;font-size:13px;font-weight:700;color:#8a8a8a;padding:6px 9px}
.select .stepper{position:absolute;right:0;top:0;width:31px;height:27px;border-left:1px solid #d0d0d0}
.filter-label{left:672px;top:481px;font-size:12px;color:#222}
.chart-frame{left:154px;top:520px;width:827px;height:268px;background:var(--panel)}
.legend{left:166px;top:532px;width:288px;height:136px;background:var(--legend);font-size:11px;color:#444}
.legend .item{position:absolute;font-size:11px}
.legend .sw{display:inline-block;width:12px;height:12px;vertical-align:-2px;margin-right:9px}
.legend .stat{position:absolute;left:45px;font-size:11px;color:#888}
.legend .tri{position:absolute;width:0;height:0;border-left:4px solid transparent;border-right:4px solid transparent}
.axis-y{left:120px;font-size:10px;font-weight:700;color:#333;width:24px;text-align:right}
.tooltip{left:621px;top:620px;width:41px;height:23px;background:#2d2d2d;border-radius:3px;color:#fff;font-size:12px;text-align:center;line-height:23px}
.tooltip:after{content:"";position:absolute;left:16px;top:23px;border-left:4px solid transparent;border-right:4px solid transparent;border-top:5px solid #2d2d2d}
.time-label{top:801px;font-size:10px;font-weight:700;color:#333;width:60px;text-align:center}
.video-frame{left:993px;top:520px;width:215px;height:268px;background:var(--panel)}
.video-still{left:998px;top:526px;width:210px;height:257px;background:linear-gradient(170deg,#22314f 0%,#3d5b82 35%,#5a2530 62%,#a01a2a 75%,#3a3a3a 100%)}
.video-controls{left:1035px;top:731px;width:175px;height:28px;background:rgba(20,20,20,.85)}
.scrubber{left:158px;top:828px;width:1060px;height:34px;border:1px solid #c4c4c4;border-radius:4px;background:linear-gradient(#fafafa,#e4e4e4)}
.scrub-label{top:846px;font-size:9px;font-weight:700;color:#444;width:40px;text-align:center}
.scrub-handle{left:630px;top:827px;width:126px;height:36px;border:1px solid #9a9a9a;border-radius:4px;background:linear-gradient(#e8e8e8,#bdbdbd)}
</style>
</head>
<body>
<div class="abs side-rail"><div class="rail-top"></div><div class="rail-nav"></div></div>
<div class="abs collapse-arrow"></div>

<header>
  <div class="abs top-bar"></div>
  <div class="abs brand-name">Lumivo</div>
  <nav class="abs main-nav"></nav>
  <svg class="abs" style="left:193px;top:98px" width="25" height="24" viewBox="0 0 25 24" aria-label="Home">
    <path d="M12.5 1 L1 11 L3.5 11 L3.5 23 L10 23 L10 16 L15 16 L15 23 L21.5 23 L21.5 11 L24 11 Z" fill="#fff"/>
    <rect x="18" y="2" width="3" height="6" fill="#fff"/>
  </svg>
  <div class="abs nav-link" style="left:299px">Projects</div>
  <div class="abs caret"></div>
  <div class="abs nav-link" style="left:422px">Result</div>
  <div class="abs nav-link" style="left:533px">Submit your Project</div>
  <div class="abs nav-link" style="left:743px">Help</div>
  <div class="abs avatar">
    <svg width="30" height="30" viewBox="0 0 30 30"><circle cx="15" cy="11" r="6" fill="#c8c8c8"/><path d="M4 30 Q15 14 26 30Z" fill="#c8c8c8"/></svg>
  </div>
  <div class="abs user-name">Nora Vell</div>
</header>

<main>
  <h1 class="abs page-title">Web design for facial<br>expression recognition</h1>
  <p class="abs meta"><span>Participants:&nbsp;&nbsp; 358</span>Stimulus :&nbsp;&nbsp; 15</p>
  <div class="abs divider"></div>

  <h2 class="abs view-title">Line Graph</h2>
  <p class="abs view-desc">Lorem ipsum dolor sit amet conse ctetur adipisicing elit, sed do eiusmod tempor incididunt ut labore et dolore magna</p>
  <div class="abs delete-btn">
    <svg class="abs" style="left:27px;top:13px" width="16" height="19" viewBox="0 0 16 19"><rect x="0" y="2" width="16" height="2" fill="#aaa"/><rect x="5" y="0" width="6" height="2" fill="#aaa"/><path d="M2 5 H14 L13 19 H3 Z" fill="#aaa"/><path d="M6 7 V17 M10 7 V17" stroke="#dcdcdc" stroke-width="1.2"/></svg>
  </div>

  <div class="abs select" style="left:157px;top:472px;width:289px">Stimulus 1<span class="stepper"><svg width="31" height="27"><path d="M12 11 L15.5 7.5 L19 11Z M12 16 L15.5 19.5 L19 16Z" fill="#444"/></svg></span></div>
  <div class="abs filter-label">Filter:</div>
  <div class="abs select" style="left:709px;top:472px;width:109px">Age 3-50<span class="stepper"><svg width="31" height="27"><path d="M12 11 L15.5 7.5 L19 11Z M12 16 L15.5 19.5 L19 16Z" fill="#444"/></svg></span></div>
  <div class="abs select" style="left:837px;top:472px;width:109px">Male<span class="stepper"><svg width="31" height="27"><path d="M12 11 L15.5 7.5 L19 11Z M12 16 L15.5 19.5 L19 16Z" fill="#444"/></svg></span></div>

  <section class="abs chart-frame"></section>
  <svg class="abs" style="left:154px;top:520px" width="827" height="268" viewBox="154 520 827 268" aria-label="Line graph of expressions over time">
    <defs><pattern id="ticks" width="8" height="6" patternUnits="userSpaceOnUse"><rect x="0" width="1" height="6" fill="#aaa"/></pattern></defs>
    <rect x="160" y="526" width="816" height="240" fill="var(--plot)"/>
    <g stroke="var(--grid)" stroke-width="1">
      <line x1="160" y1="566.5" x2="976" y2="566.5"/><line x1="160" y1="606.5" x2="976" y2="606.5"/>
      <line x1="160" y1="646.5" x2="976" y2="646.5"/><line x1="160" y1="686.5" x2="976" y2="686.5"/>
      <line x1="160" y1="726.5" x2="976" y2="726.5"/>
    </g>
    <rect x="160" y="766" width="816" height="19" fill="#dedede"/>
    <g stroke="#999" stroke-width="1">
      <path d="M272.5 770 V785 M392.5 770 V785 M512.5 770 V785 M632.5 770 V785 M752.5 770 V785 M872.5 770 V785"/>
    </g>
    <rect x="160" y="779" width="816" height="6" fill="url(#ticks)"/>
    <polyline fill="none" stroke="var(--blue)" stroke-width="1.3" points="197,684 219,690 227,712 232,684 240,674 300,667 328,674 350,706 378,733 398,658 405,670 428,671 447,685 479,681 517,708 546,695 578,704 600,750 630,664 650,727 658,712 690,700 710,704 735,720 759,745 780,700 822,719 848,666 869,690 893,716 920,752 948,740 966,705"/>
    <polyline fill="none" stroke="var(--green)" stroke-width="1.3" points="193,740 240,688 260,734 293,729 307,714 356,702 400,750 490,750 550,735 600,705 642,660 662,740 680,720 710,668 733,602 798,597 852,623 873,705 895,757 925,670 945,653 967,645"/>
    <line x1="687.5" y1="526" x2="687.5" y2="770" stroke="#555" stroke-width="1"/>
    <rect x="680" y="764" width="14" height="22" rx="3" fill="var(--marker)" stroke="#9a6a05"/>
    <path d="M687 760 L681 766 H693Z" fill="var(--marker)"/>
  </svg>
  <div class="abs axis-y" style="top:540px">1</div>
  <div class="abs axis-y" style="top:580px">0.8</div>
  <div class="abs axis-y" style="top:620px">0.6</div>
  <div class="abs axis-y" style="top:660px">0.4</div>
  <div class="abs axis-y" style="top:700px">0.2</div>
  <div class="abs axis-y" style="top:740px">0</div>

  <div class="abs legend">
    <div class="item" style="left:13px;top:9px"><span class="sw" style="background:var(--green)"></span>Neutral</div>
    <span class="tri" style="left:121px;top:13px;border-bottom:5px solid #666"></span>
    <div class="stat" style="top:30px">High:&nbsp; 0.8</div>
    <div class="stat" style="top:49px">Avg.:&nbsp;&nbsp; 0.35</div>
    <div class="stat" style="top:67px">Low:&nbsp; 0.15</div>
    <div class="stat" style="top:86px">St. Dev.&nbsp; 0.05</div>
    <div class="item" style="left:13px;top:110px"><span class="sw" style="background:var(--blue)"></span>Sad</div>
    <span class="tri" style="left:121px;top:114px;border-top:5px solid #666"></span>
    <div class="item" style="left:161px;top:9px"><span class="sw" style="background:var(--red)"></span>Angry</div>
    <span class="tri" style="left:268px;top:14px;border-top:5px solid #666"></span>
    <div class="item" style="left:161px;top:29px"><span class="sw" style="background:var(--pink)"></span>Joy</div>
    <span class="tri" style="left:268px;top:34px;border-top:5px solid #666"></span>
  </div>
  <div class="abs tooltip">20</div>

  <div class="abs time-label" style="left:167px">00:02.00</div>
  <div class="abs time-label" style="left:229px">00:04.00</div>
  <div class="abs time-label" style="left:290px">00:06.00</div>
  <div class="abs time-label" style="left:352px">00:08.00</div>
  <div class="abs time-label" style="left:413px">00:10.00</div>
  <div class="abs time-label" style="left:475px">00:12.00</div>
  <div class="abs time-label" style="left:536px">00:14.00</div>
  <div class="abs time-label" style="left:598px">00:16.00</div>
  <div class="abs time-label" style="left:660px">00:18.00</div>
  <div class="abs time-label" style="left:721px">00:20.00</div>
  <div class="abs time-label" style="left:783px">00:22.00</div>
  <div class="abs time-label" style="left:844px">00:24.00</div>
  <div class="abs time-label" style="left:906px">00:26.00</div>

  <section class="abs video-frame"></section>
  <div class="abs video-still" role="img" aria-label="Stimulus video frame: red sports car in front of mountains under a night sky"></div>
  <div class="abs video-controls">
    <svg width="175" height="28" viewBox="0 0 175 28">
      <path d="M11 14 L17 9 V19Z M17 14 L23 9 V19Z" fill="#ddd"/>
      <path d="M48 8 L58 14 L48 20Z" fill="#ddd"/>
      <path d="M84 9 L90 14 L84 19Z M90 9 L96 14 L90 19Z" fill="#ddd"/>
      <path d="M119 11 H122 L126 8 V20 L122 17 H119Z" fill="#ddd"/>
      <path d="M150 10 H158 M150 14 H158 M150 18 H158" stroke="#ddd" stroke-width="1.6"/>
      <path d="M37 0 V28 M73 0 V28 M108 0 V28 M139 0 V28" stroke="#444"/>
    </svg>
  </div>

  <div class="abs scrubber">
    <svg width="1060" height="34" viewBox="0 0 1060 34">
      <defs><pattern id="minor" width="12" height="6" patternUnits="userSpaceOnUse"><rect width="1" height="6" fill="#b5b5b5"/></pattern></defs>
      <rect x="0" y="0" width="1060" height="6" fill="url(#minor)"/>
      <path d="M115.5 0 V34 M235.5 0 V34 M355.5 0 V34 M475.5 0 V34 M715.5 0 V34 M835.5 0 V34 M955.5 0 V34" stroke="#c4c4c4"/>
    </svg>
  </div>
  <div class="abs scrub-handle"></div>
  <div class="abs scrub-label" style="left:192px">1:00</div>
  <div class="abs scrub-label" style="left:313px">1:00</div>
  <div class="abs scrub-label" style="left:432px">1:00</div>
  <div class="abs scrub-label" style="left:553px">1:00</div>
  <div class="abs scrub-label" style="left:672px">1:00</div>
  <div class="abs scrub-label" style="left:794px">1:00</div>
  <div class="abs scrub-label" style="left:912px">1:00</div>
  <div class="abs scrub-label" style="left:1032px">1:00</div>
  <div class="abs scrub-label" style="left:1152px">1:00</div>
</main>
</body>
</html>
```